Brochure Design - Non-Profit Fundraising Stream

We are a non-profit organization that is developing a fundraising project through the donation of life insurance policies. We have three brochures in each English and French that we developed for a sister organization that we want to reintegrate with our Foundation, keeping the same copy text just changing the logos, colors and make it overall more visually appealing. The foundation is called the 'Varnek-Holt Syndrome Foundation Canada'.
The original files in .docx format are attached as is the full logo and two symbol files. The deliverables would be six documents in total (InDesign or .docx), each brochure in English and French. The color hex codes are:
red: #7b2850
dark blue: #2c79a7
pale blue: #78b2e2

```html
<!DOCTYPE html>
<html lang="en">
<head>
<meta charset="utf-8">
<title>Life Insurance Donation Brochure – Varnek-Holt Syndrome Foundation Canada</title>
<link href="https://fonts.googleapis.com/css2?family=Montserrat:wght@400;500;600;700&family=Crimson+Pro:wght@600;700&display=swap" rel="stylesheet">
<style>
:root{
  --red:#7b2850;
  --red-dark:#5e1b3c;
  --blue:#2c79a7;
  --blue-dark:#1d5f8a;
  --pale:#78b2e2;
  --ink:#2b2b2b;
  --page:#ffffff;
  --bg:#e6e6e6;
}
*{margin:0;padding:0;box-sizing:border-box}
html,body{width:1200px;height:907px;overflow:hidden;background:var(--bg)}
body{position:relative;font-family:"Montserrat",sans-serif;color:var(--ink)}
.page{position:absolute;top:100px;width:490px;height:680px;background:var(--page);overflow:hidden;box-shadow:0 4px 14px rgba(0,0,0,.25)}
.page--front{left:70px}
.page--back{left:640px}
.page-art{position:absolute;inset:0;width:100%;height:100%}
.abs{position:absolute}
.serif-head{font-family:"Crimson Pro",serif;font-weight:700;letter-spacing:.06em;text-transform:uppercase}

/* front */
.brand{left:26px;top:26px;color:#fff;font-size:17px;font-weight:500;line-height:1.15;width:190px}
.headline{left:30px;top:78px;color:#fff;font-size:20px;font-weight:500;line-height:1.25}
.headline strong{display:block;color:var(--pale);font-size:28px;font-weight:700;margin-top:2px}
.intro{left:26px;top:272px;width:440px;font-size:9.2px;line-height:1.38}
.pill{background:linear-gradient(90deg,var(--blue-dark),var(--pale));color:#fff;font-size:13px;padding:4px 22px 3px 26px;border-radius:0 14px 14px 0}
.pill--front{left:0;top:346px}
.bullets{list-style:none;font-size:9.2px;line-height:1.35}
.bullets li{position:relative;padding-left:14px;margin-bottom:6px}
.bullets li::before{content:"";position:absolute;left:0;top:3px;width:6px;height:6px;background:var(--blue);border-radius:50% 50% 50% 0;transform:rotate(-45deg)}
.bullets--light li::before{background:#fff}
.policy-cols{left:28px;top:387px;display:flex;gap:50px}
.policy-cols ul{width:200px}
.boxed-title{border:1.5px solid currentColor;text-align:center;padding:5px 10px 3px}
.advantages-title{left:26px;top:474px;width:438px;color:#fff;font-size:14.5px}
.advantages{left:28px;top:516px;width:430px;color:#fff}

/* back */
.independence-title{left:90px;top:24px;width:310px;color:var(--blue-dark);font-size:14.5px;border-color:var(--blue)}
.independence{left:30px;top:66px;width:245px}
.photo-circle{left:275px;top:88px;width:200px;height:200px;border-radius:50%;border:5px solid #fff;box-shadow:0 0 0 4px var(--pale);background:radial-gradient(circle at 45% 40%,#c9533a 0%,#5a3a2c 35%,#2a2320 75%)}
.photo-hands{left:272px;top:0;width:218px;height:210px;background:linear-gradient(135deg,#8a7a68,#d8c8b6 45%,#a08468)}
.pill--back{left:0;top:243px;border-radius:0 14px 14px 0}
.steps{left:16px;top:276px;display:flex;align-items:center;gap:4px}
.step{width:78px;height:122px;border:1.5px solid rgba(255,255,255,.9);border-radius:0 14px 0 14px;color:#fff;font-size:8px;line-height:1.25;text-align:center;display:flex;flex-direction:column;align-items:center;padding:8px 4px 0}
.step svg{width:36px;height:36px;margin-bottom:10px}
.step span{flex:1;display:flex;align-items:center}
.arrow{width:12px;height:14px}
.disclosures-title{left:170px;top:434px;width:150px;color:var(--blue-dark);font-size:14.5px;border-color:var(--blue)}
.disclosures{left:30px;top:474px;width:440px}
.footer{left:0;top:612px;width:490px;height:68px;display:flex;align-items:center;padding-left:28px;color:#fff}
.footer .call{font-family:"Crimson Pro",serif;font-weight:700;font-size:16px;letter-spacing:.06em;padding-right:12px;border-right:1.5px solid #fff;margin-right:10px;line-height:28px}
.footer .phone{font-family:"Crimson Pro",serif;font-weight:700;font-size:18px}
.footer .email{font-family:"Crimson Pro",serif;font-size:15px;margin-left:6px;padding-left:6px;border-left:1.5px solid #fff}
</style>
</head>
<body>

<section class="page page--front" aria-label="Brochure front">
  <svg class="page-art" viewBox="0 0 490 680" aria-hidden="true">
    <defs>
      <linearGradient id="blueFront" x1="0" y1="0" x2="1" y2="1">
        <stop offset="0" stop-color="#2c79a7"/><stop offset="1" stop-color="#1d5f8a"/>
      </linearGradient>
    </defs>
    <path d="M0 0H490V200C380 250 200 265 0 240Z" fill="url(#blueFront)"/>
    <path d="M0 200C120 265 320 250 490 165V215C360 272 170 285 0 258Z" fill="#7b2850"/>
    <path d="M0 236C140 270 330 255 490 190" fill="none" stroke="#fff" stroke-width="3"/>
    <path d="M0 248C150 282 340 262 490 205" fill="none" stroke="#78b2e2" stroke-width="1.5"/>
    <path d="M0 470C140 440 340 448 490 475V640H0Z" fill="#7b2850"/>
    <path d="M0 640H490V680H0Z" fill="#fff"/>
    <path d="M0 636C160 650 330 652 490 636" fill="none" stroke="#78b2e2" stroke-width="1.5"/>
  </svg>
  <div class="abs photo-hands" role="img" aria-label="Photo of cupped hands holding a paper-cut family" style="border-radius:0 0 0 70%/0 0 0 60%;border-left:5px solid #fff;border-bottom:5px solid #fff"></div>
  <p class="abs brand">Varnek-Holt Syndrome Foundation Canada</p>
  <h1 class="abs headline">Unlock the<br>Hidden value in our<strong>Life Insurance</strong></h1>
  <p class="abs intro">You can maintain or substantially improve your financial position by unlocking the hidden value of your unwanted or unaffordable life insurance via a charitable donation. Every year, seniors over the age of 70 lapse or surrender almost $7 billion of insurance that they might otherwise donate to a charity. You can pay down debt, make major purchases or replenish retirement savings by accessing the value you deserve after paying premiums for decades.</p>
  <h2 class="abs pill pill--front serif-head">Suitable Policies</h2>
  <div class="abs policy-cols">
    <ul class="bullets"><li>Term, Whole life, Universal or term-to-100 policies</li><li>Insured lives over 70 years old</li></ul>
    <ul class="bullets"><li>In-force greater than 2 years</li><li>Minimum death benefit of $50,000</li></ul>
  </div>
  <h2 class="abs boxed-title advantages-title serif-head">Advantages of Donating a Life Insurance Policy</h2>
  <ul class="abs bullets bullets--light advantages">
    <li>You obtain a tax receipt (good for 5 years) for 10%-50% of the face value of the policy (even for term policies that have no "cash surrender value")</li>
    <li>You convert a "worthless or low cash value policy" into cash in your pocket when you file your income taxes</li>
    <li>Eliminate the burden of annual premium expenses</li>
    <li>A Foundation becomes the owner and beneficiary, and it funds the premiums and collects the benefit upon maturity</li>
  </ul>
</section>

<section class="page page--back" aria-label="Brochure back">
  <svg class="page-art" viewBox="0 0 490 680" aria-hidden="true">
    <path d="M0 150C120 170 220 205 300 215V250C200 240 100 225 0 215Z" fill="#2c79a7"/>
    <path d="M0 205C140 220 320 250 490 220V405C350 440 150 432 0 400Z" fill="#7b2850"/>
    <path d="M0 198C140 214 320 244 490 212" fill="none" stroke="#fff" stroke-width="3"/>
    <path d="M0 412C150 444 350 450 490 414" fill="none" stroke="#78b2e2" stroke-width="1.5"/>
    <path d="M0 612H490V680H0Z" fill="#2c79a7"/>
  </svg>
  <h2 class="abs boxed-title independence-title serif-head">Maintain Financial Independence</h2>
  <ul class="abs bullets independence">
    <li>Fund retirement living or long-term care expenses through lowered income taxes as a result of the tax receipt</li>
    <li>Reallocate proceeds from the tax receipt and savings to income producing financial assets or annuities</li>
    <li>Reduce or pay off outstanding debts</li>
  </ul>
  <div class="abs photo-circle" role="img" aria-label="Photo of wooden figures sheltered under a drawn red umbrella"></div>
  <h2 class="abs pill pill--back serif-head">Suitable Policies</h2>
  <div class="abs steps">
    <div class="step">
      <svg viewBox="0 0 36 36" fill="none" stroke="#fff" stroke-width="1.8"><circle cx="18" cy="18" r="17" fill="#fff" stroke="none"/><rect x="11" y="9" width="14" height="18" rx="1.5" stroke="#7b2850"/><path d="M14 15h8M14 19h8M14 23h5" stroke="#7b2850"/></svg>
      <span>Complete Application Form &amp; Provide Policy Documents and Illustration</span>
    </div>
    <svg class="arrow" viewBox="0 0 12 14" fill="none" stroke="#fff" stroke-width="1.4"><path d="M1 4h5V1l5 6-5 6v-3H1Z"/></svg>
    <div class="step">
      <svg viewBox="0 0 36 36"><circle cx="18" cy="18" r="17" fill="#fff"/><path d="M15 10h6v5h5v6h-5v5h-6v-5h-5v-6h5Z" fill="#7b2850"/></svg>
      <span>Provide Medical Information</span>
    </div>
    <svg class="arrow" viewBox="0 0 12 14" fill="none" stroke="#fff" stroke-width="1.4"><path d="M1 4h5V1l5 6-5 6v-3H1Z"/></svg>
    <div class="step">
      <svg viewBox="0 0 36 36" fill="none"><circle cx="18" cy="18" r="17" fill="#fff"/><rect x="10" y="9" width="13" height="17" stroke="#7b2850" stroke-width="1.8"/><circle cx="24" cy="23" r="5" fill="#7b2850"/><path d="M13 14h7M13 18h5" stroke="#7b2850" stroke-width="1.8"/></svg>
      <span>Determine Amount of Tax Receipt</span>
    </div>
    <svg class="arrow" viewBox="0 0 12 14" fill="none" stroke="#fff" stroke-width="1.4"><path d="M1 4h5V1l5 6-5 6v-3H1Z"/></svg>
    <div class="step">
      <svg viewBox="0 0 36 36" fill="none"><circle cx="18" cy="18" r="17" fill="#fff"/><rect x="12" y="8" width="13" height="18" fill="#7b2850"/><path d="M15 13h7M15 17h7M15 21h5" stroke="#fff" stroke-width="1.5"/></svg>
      <span>Sign Ownership Transfer Documents</span>
    </div>
    <svg class="arrow" viewBox="0 0 12 14" fill="none" stroke="#fff" stroke-width="1.4"><path d="M1 4h5V1l5 6-5 6v-3H1Z"/></svg>
    <div class="step">
      <svg viewBox="0 0 36 36"><circle cx="18" cy="18" r="17" fill="#fff"/><ellipse cx="15" cy="12" rx="6" ry="2.5" fill="#7b2850"/><ellipse cx="15" cy="17" rx="6" ry="2.5" fill="#7b2850"/><ellipse cx="15" cy="22" rx="6" ry="2.5" fill="#7b2850"/><circle cx="23" cy="22" r="5.5" fill="#7b2850" stroke="#fff" stroke-width="1"/></svg>
      <span>Convert the Tax Receipt into $$$ in your Pocket</span>
    </div>
  </div>
  <h2 class="abs boxed-title disclosures-title serif-head">Disclosures</h2>
  <ul class="abs bullets disclosures">
    <li>Proceeds are treated as a disposition for tax purposes and are taxed on excess amount over adjusted cost basis, which includes all premiums paid on the policy less the net cost of pure insurance. Policyholders should seek their own independent professional tax, legal and financial advice.</li>
    <li>A change of ownership of a policy may in the future limit the insured's ability to purchase additional insurance as a result of limits on how much coverage insurers will issue.</li>
    <li>Donors of life insurance policies will be required to provide consent to allow access to medical records for purposes of evaluating the life insurance policy. This information will be maintained on a confidential basis.</li>
  </ul>
  <div class="abs footer">
    <span class="call">CALL US</span>
    <span class="phone">1(800) 555-0147</span>
    <span class="email">info@varnekholtcanada.org</span>
  </div>
</section>

</body>
</html>
```